KALVENTO Amazing Business Cards Challenge

Kalvent is a new technology company that will provide engineering and manufacturing services in the electric vehicle industry.

We are looking at a new business card that will support our orientation in providing advanced, innovative solutions. The business card will be lean and present the only information required to be more efficient.

Target Market(s)

Fleet operators, private commercial vehicle operators, delivery companies.

Industry/Entity Type

Business

Contact Information for Business Card

Use the logo and its colors, use a white background.

Font styles to use
Sans Serif

Colors
0455a3
ffffff
9bcb3c

Requirements
Must have
• Kalvento Logo
• All informations in the DOC file = 3 different cards.
• White background
Nice to have
• Icons for email, phone and web address.
• Cute design and strong identity.
Should not have
• Bleeds

```html
<!DOCTYPE html>
<html lang="en">
<head>
<meta charset="utf-8">
<title>Kalvento Business Cards</title>
<link href="https://fonts.googleapis.com/css2?family=Open+Sans:wght@400;600;700&display=swap" rel="stylesheet">
<style>
  :root{
    --bg:#d9d9d9;
    --card:#ffffff;
    --brand-blue:#1a6fae;
    --deep-blue:#0d4f8a;
    --ink-gray:#3f3f42;
    --soft-gray:#6b6b6e;
    --line-gray:#8a8a8d;
  }
  *{margin:0;padding:0;box-sizing:border-box}
  html,body{width:1200px;height:852px;overflow:hidden}
  body{background:var(--bg);font-family:"Open Sans",sans-serif;position:relative}
  .card{position:absolute;width:540px;height:310px;background:var(--card);border-radius:22px;overflow:hidden;box-shadow:0 6px 18px rgba(0,0,0,.18)}
  .card--front{left:60px;top:90px}
  .card--back{left:600px;top:450px}

  .wordmark{font-weight:600;color:var(--ink-gray);letter-spacing:1px;line-height:1}
  .card--front .wordmark{position:absolute;left:0;right:0;top:100px;text-align:center;font-size:78px}
  .web-line{position:absolute;left:0;right:0;top:232px;display:flex;align-items:center;justify-content:center;gap:16px}
  .web-line .rule{width:90px;height:1px;background:var(--line-gray)}
  .web-line .url{font-size:14px;color:var(--brand-blue);letter-spacing:.5px}

  .card--back .wordmark{position:absolute;left:36px;top:112px;font-size:50px}
  .back-art{position:absolute;inset:0}
  .person{position:absolute;right:22px;top:14px;text-align:right}
  .person .name{font-size:17px;font-weight:700;color:var(--brand-blue);line-height:1.3}
  .person .name .creds{font-weight:400}
  .person .role{font-size:11px;color:var(--soft-gray);line-height:1.35}
  .contact{position:absolute;right:22px;top:120px;list-style:none;text-align:right;color:#fff;font-size:12px;line-height:19px}
  .contact li{display:flex;justify-content:flex-end;align-items:center;gap:6px}
  .contact li.plain{padding-right:17px}
  .contact svg{width:11px;height:11px;flex:none}
</style>
</head>
<body>

<section class="card card--front">
  <div class="wordmark">kalvento</div>
  <div class="web-line">
    <span class="rule"></span>
    <span class="url">www.kalvento.com</span>
    <span class="rule"></span>
  </div>
</section>

<section class="card card--back">
  <svg class="back-art" viewBox="0 0 540 310" preserveAspectRatio="none" aria-hidden="true">
    <defs>
      <linearGradient id="waveBlue" x1="0" y1="0" x2="1" y2="1">
        <stop offset="0" stop-color="#1a6fae"/>
        <stop offset="1" stop-color="#0d4f8a"/>
      </linearGradient>
    </defs>
    <path d="M560,92 L540,92 C440,94 360,105 330,150 C300,215 210,268 0,278 L0,310 L560,310 Z" fill="url(#waveBlue)"/>
    <path d="M560,92 L540,92 C440,94 360,105 330,150 C300,215 210,268 0,278" transform="translate(-5,-8)" fill="none" stroke="#3f3f42" stroke-width="6"/>
    <path d="M560,92 L540,92 C440,94 360,105 330,150 C300,215 210,268 0,278" transform="translate(-11,-16)" fill="none" stroke="#8a8a8d" stroke-width="1.5"/>
    <path d="M0,298 C180,300 300,292 380,262" fill="none" stroke="#5aa0d6" stroke-width="4"/>
  </svg>

  <div class="wordmark">kalvento</div>

  <div class="person">
    <div class="name">Mathieu Lavergne, <span class="creds">ing.,M.Sc.A.</span></div>
    <div class="role">V.P. Développement des affaires<br>V.P. Business Development</div>
  </div>

  <ul class="contact">
    <li>+1.514.555.0187
      <svg viewBox="0 0 12 12"><path d="M2 1h2.5l1 2.5-1.5 1a6 6 0 0 0 3.5 3.5l1-1.5 2.5 1V11C5.5 11 1 6.5 1 2z" fill="#fff"/></svg></li>
    <li>www.kalvento.com
      <svg viewBox="0 0 12 12"><circle cx="6" cy="6" r="5" fill="none" stroke="#fff" stroke-width="1.2"/><path d="M1 6h10M6 1c2.5 3 2.5 7 0 10M6 1c-2.5 3-2.5 7 0 10" fill="none" stroke="#fff" stroke-width="1"/></svg></li>
    <li>mlavergne@kalvento.com
      <svg viewBox="0 0 12 12"><rect x="1" y="2.5" width="10" height="7" fill="#fff"/><path d="M1 2.5l5 4 5-4" fill="none" stroke="#0d4f8a" stroke-width="1"/></svg></li>
    <li>410 - 220 Rue Belmont
      <svg viewBox="0 0 12 12"><path d="M6 11S2 6.8 2 4.5a4 4 0 0 1 8 0C10 6.8 6 11 6 11z" fill="#fff"/><circle cx="6" cy="4.5" r="1.4" fill="#0d4f8a"/></svg></li>
    <li class="plain">Laval (Québec) H7N 2K5 Canada</li>
  </ul>
</section>

</body>
</html>
```